New River III Precinct 6x11 GOTV postcard

We require BOTH persuasive copy and high-impact layout for an oversized 6x11 political mailer. This might be one person, but it likely requires a specialized "creative team." of an experienced political strategist copywriter PLUS a graphic designer - so the words fit the exact layout block, and the visuals reinforce the psychological punch of the headline.

The goal is to remove all excuses a targeted audience of ~900 registered Harvestline + ~1800 Unaffiliated voters in our precinct - have for not voting.

I need to be able to work by phone / online chat to iterate designs
I need to own the design in the top couple of software outputs that any printer service will require.

I want to experiment with very subtle background images as follows:
- Front of postcard that conveys "CHANGE" of not just seasons - but of encouraging change of precinct voter representation - so anything about fall foliage / conveyance of change tie-in is worthy of considering
- Back of postcard - any Appalachian long rage mountain view that includes 5-7 layers of hills in the distance.
Some photos as samples to consider.

Target Market(s)

~2,700 registered Harvestliners and Unaffiliated voters

Requirements
Must have
• We require BOTH persuasive copy and high-impact layout for an oversized 6x11 political mailer. This might be one person, but it likely requires a specialized "creative team." of an experienced political strategist copywriter PLUS a graphic designer - so the words fit the exact layout block, and the visuals reinforce the psychological punch of the headline
Nice to have
• subtle background photos

```html
<!DOCTYPE html>
<html lang="en">
<head>
<meta charset="utf-8">
<title>New River III Precinct GOTV Postcard</title>
<link href="https://fonts.googleapis.com/css2?family=Poppins:wght@700&family=Source+Sans+3:wght@400;600;700&display=swap" rel="stylesheet">
<style>
:root{
  --navy:#2b2a66;
  --navy-deep:#24235a;
  --red:#b01f2a;
  --red-dark:#8e1720;
  --red-text:#a81d27;
  --white:#ffffff;
  --ink:#1f1f4d;
  --muted:#3a3a3a;
  --backdrop:#8a8a8a;
  --panel-grey:#e6e6e6;
  --leaf:#f0a43a;
  --leaf-deep:#e07b2a;
}
*{margin:0;padding:0;box-sizing:border-box}
html,body{width:1133px;height:1200px;overflow:hidden}
body{background:var(--backdrop);font-family:"Source Sans 3",Arial,sans-serif;position:relative}
.card{position:absolute;left:95px;width:944px;height:515px;background:var(--white);overflow:hidden}
.front{top:54px}
.back{top:599px}

/* FRONT */
.front-hero{position:absolute;left:0;top:0;width:944px;height:349px;
  background:linear-gradient(160deg,var(--navy) 0%,#33327a 45%,var(--navy-deep) 100%)}
.front-rule{position:absolute;left:0;top:349px;width:944px;height:10px;background:var(--red)}
.headline{position:absolute;left:36px;top:36px;font-family:"Poppins",sans-serif;font-weight:700;
  color:var(--white);font-size:82px;line-height:1;letter-spacing:-1.5px}
.ribbon{position:absolute;left:34px;top:115px;width:436px;height:48px}
.ribbon-text{position:absolute;left:34px;top:115px;width:436px;height:40px;line-height:42px;text-align:center;
  font-family:"Poppins",sans-serif;font-weight:700;font-size:30px;color:var(--white)}
.issue{position:absolute;color:var(--white)}
.issue h3{font-weight:700;font-size:12.5px;line-height:1.2;margin-bottom:1px}
.issue p{font-size:9.4px;line-height:1.3}
.issue strong{font-weight:700}
.divider{position:absolute;left:489px;top:52px;width:1px;height:274px;background:rgba(255,255,255,.7)}
.leaf-spot{position:absolute;border-radius:50% 10% 50% 50%}
.leaf-divider{left:456px;top:189px;width:68px;height:70px;background:radial-gradient(circle,var(--leaf) 55%,#d98a25 100%)}
.leaf-corner{left:884px;top:336px;width:60px;height:72px;background:radial-gradient(circle,var(--leaf-deep) 55%,#c9621f 100%)}
.leaf-faint{position:absolute;left:160px;top:395px;width:240px;height:120px;border-radius:40%;
  background:radial-gradient(ellipse,rgba(240,190,130,.3) 0%,rgba(240,190,130,0) 70%)}
.ballot-title{position:absolute;font-weight:700;font-size:14.5px;line-height:1.2;color:var(--red-text)}
.race{position:absolute}
.race h4{font-weight:700;font-size:12px;color:var(--ink);line-height:1.2}
.race p{font-size:9px;color:var(--muted);text-transform:uppercase;line-height:1.3}

/* BACK */
.letter{position:absolute;left:0;top:0;width:489px;height:246px;background:var(--navy);color:var(--white);padding:31px 30px 0 44px}
.letter h2{font-weight:700;font-size:14px;margin-bottom:8px}
.letter p{font-size:9.6px;line-height:1.3;margin-bottom:9px;max-width:412px}
.back-bar{position:absolute;left:489px;top:0;width:6px;height:515px;background:var(--red)}
.checklist{position:absolute;left:48px;top:257px;list-style:none;width:430px}
.checklist li{position:relative;padding-left:16px;font-weight:600;font-size:12px;color:var(--red-text);
  height:19px;line-height:19px;display:flex;align-items:center}
.checklist li::before{content:"";position:absolute;left:2px;top:6px;width:7px;height:7px;border-radius:50%;background:var(--navy)}
.checklist .value{color:#111;margin-left:4px;font-weight:600}
.checklist .fill-line{flex:1;height:1px;background:#9a9a9a;margin:6px 0 0 6px}
.checklist li.gap{margin-top:2px}
.scenery{position:absolute;left:0;top:383px;width:495px;height:132px;
  background:linear-gradient(180deg,#f8c46e 0%,#f6a83e 35%,#e98a2c 55%,#8e3a26 78%,#6b2a22 100%)}
.address-side{position:absolute;left:495px;top:0;width:449px;height:515px;background:var(--white)}
.indicia{position:absolute;left:819px;top:36px;width:90px;height:86px;background:var(--panel-grey);
  font-size:11.5px;line-height:1.35;color:#222;text-align:center;padding-top:9px}
.address{position:absolute;left:598px;top:150px;width:265px;height:108px;background:#f2f2f2;
  display:flex;align-items:center;justify-content:center;text-align:center;font-size:12.5px;line-height:1.3;color:#222}
</style>
</head>
<body>

<section class="card front" aria-label="Postcard front">
  <div class="front-hero"></div>
  <div class="front-rule"></div>

  <h1 class="headline">VOTE FOR</h1>
  <svg class="ribbon" viewBox="0 0 436 48" aria-hidden="true">
    <polygon points="0,10 26,10 26,42 0,42 10,26" fill="#8e1720"/>
    <polygon points="436,10 410,10 410,42 436,42 426,26" fill="#8e1720"/>
    <rect x="24" y="2" width="388" height="38" fill="#b01f2a"/>
  </svg>
  <div class="ribbon-text">NEW REPRESENTATION</div>

  <div class="issue" style="left:38px;top:189px;width:348px">
    <h3>LOCAL PAIN-THANKS TO CURRENT REPRESENTATIVES</h3>
    <p>and sadly, to avoid accountability, they’ve cleverly delayed many / most impacts until after the 2026 election. <strong>VOTE FOR CHANGE</strong></p>
  </div>
  <div class="issue" style="left:38px;top:242px;width:380px">
    <h3>FAMILY BUDGET</h3>
    <p>exploded costs for everything: groceries, gas, car insurance, rent.</p>
  </div>
  <div class="issue" style="left:38px;top:282px;width:372px">
    <h3>HEALTH</h3>
    <p>expired subsidies, tax credits mean ~1m in NC will lose coverage or pay more. 50% cuts to Hospitals, Mental Health facilities; rural facilities will be closing</p>
  </div>

  <div class="divider"></div>
  <div class="leaf-spot leaf-divider" role="img" aria-label="Golden maple leaf illustration"></div>

  <div class="issue" style="left:544px;top:58px;width:360px">
    <h3>EDUCATION</h3>
    <p>Watauga $2.2mm shortfall personnel cuts, freezes in hiring, teacher training. Abandoning civil rights of Special Ed students to HHS and DOL</p>
  </div>
  <div class="issue" style="left:544px;top:113px;width:360px">
    <h3>HOUSING</h3>
    <p>25% of renters are spending over 50% of income on rent. Especially bad locally; predatory leasing terms and skyrocketing rents. Proposed legislation is transforming HUD with the goal of getting rid of Section 8 housing that cares for vulnerable populations.</p>
  </div>
  <div class="issue" style="left:544px;top:180px;width:345px">
    <h3>ENERGY</h3>
    <p>In 2022 Boone achieved 100% renewable energy in town buildings; this is now being destroyed by repeal of renewable energy project funding. Highland State Innovation District prepares renewable workforce technologies-all this is now in limbo.</p>
  </div>
  <div class="issue" style="left:544px;top:254px;width:338px">
    <h3>ENVIRONMENT</h3>
    <p>Reduced protections from coal ash pond leaks threaten public health. Corporations not held responsible for damage; public picks up the tab. Environmental Justice enforcement no longer a priority. Logging in Watauga with no public oversight. It’s the "haz-mat" model do nothing, wait for catastrophe, then fix it</p>
  </div>

  <div class="leaf-spot leaf-corner" role="img" aria-label="Orange maple leaf illustration"></div>
  <div class="leaf-faint" role="img" aria-label="Faint falling autumn leaves"></div>

  <h2 class="ballot-title" style="left:47px;top:379px">SAMPLE BALLOT RECOMMENDATIONS</h2>
  <h2 class="ballot-title" style="left:361px;top:378px">REQMT TO SHOW ID FOR VOTERS NOT IN PERSON-NO</h2>

  <div class="race" style="left:47px;top:402px"><h4>US SENATE</h4><p>Ray Calloway</p></div>
  <div class="race" style="left:47px;top:438px"><h4>US HOUSE-DISTRICT 5</h4><p>Chet Holloway</p></div>

  <div class="race" style="left:361px;top:402px"><h4>STATE SENATE DISTRICT 47</h4><p>Frank Dunmore</p></div>
  <div class="race" style="left:544px;top:402px"><h4>HOUSE OF REP’S DISTRICT 93</h4><p>Charles Whitley</p></div>
  <div class="race" style="left:738px;top:402px"><h4>NC SUPREME COURT</h4><p>Anita Ellison</p></div>

  <div class="race" style="left:360px;top:442px"><h4>NC COURT OF APPEALS-SEAT 1</h4><p>John Ashgrove</p></div>
  <div class="race" style="left:544px;top:442px"><h4>NC COURT OF APPEALS-SEAT 2</h4><p>Toby Hartwell</p></div>
  <div class="race" style="left:738px;top:442px"><h4>NC COURT OF APPEALS-SEAT 3</h4><p>Christine Walbeck</p></div>
</section>

<section class="card back" aria-label="Postcard back">
  <div class="letter">
    <h2>Dear New River III Neighbor,</h2>
    <p>We live in a representative democracy. We expect our representatives will exercise independent thinking and support policies and legislation that don’t harm us and that reflect the MAJORITY VIEWS of precinct citizens.</p>
    <p>But our current representatives HAVE STOPPED LISTENING - they are now bringing harmful policies straight to Watauga County. IT’S TIME TO HOLD THEM ACCOUNTABLE AND VOTE THEM OUT.</p>
    <p>Make no mistake: in 2026, every election is partisan. Even Judicial seats are now tied directly to state platforms.</p>
    <p>Any candidate who refuses to publicly condemn Raleigh’s gerrymandered overreach into Watauga politics-or refuses to fight funding cuts for our healthcare, education, and environmental justice is actively supporting these harmful policies</p>
    <p>They are hoping their silence fools you. DON’T BE FOOLED. This November, VOTE FOR CHANGE.</p>
  </div>

  <ul class="checklist">
    <li>YOU ARE A REGISTERED VOTER IN WATAUGA COUNTY</li>
    <li>YOU RESIDE IN PRECINCT: <span class="value">NEW RIVER III</span></li>
    <li>POLLING PLACES AVAILABLE TO YOU ARE: <span class="value">LOCATION,. 2, 3</span></li>
    <li class="gap">EARLY VOTING STARTS ON <span class="fill-line"></span></li>
    <li class="gap">DEADLINE TO APPLY FOR MAIL-IN BALLOTS <span class="fill-line"></span></li>
    <li class="gap" style="margin-top:6px">KNOW THE RULES TO ENSURE YOUR MAIL-IN-BALLOT COUNTS</li>
  </ul>

  <div class="scenery" role="img" aria-label="Layered Appalachian mountain ridges at sunset"></div>
  <div class="back-bar"></div>
  <div class="address-side"></div>

  <div class="indicia">PRSRT STD<br>ECRWSS<br>U.S. Postage<br>PAID<br>EDDM Retail</div>
  <div class="address">LOCAL POSTAL<br>CUSTOMER</div>
</section>

</body>
</html>
```